Memorial Ledger Suite (Web Design)

Design with your logo. Background in black or dark. Elegant style, it's a website for professional people only. Our company provides a cloud software manager for Funeral Services Companies.

Target Market(s)

Professional of Funeral Services.

Coding

Coded - Design and coding required

Number of Pages Required

3 page

Font styles to use
Sans Serif

Colors
fbee3d
000000
5c5c5c

Requirements
Must have
• Design of the website should be similar to our logo colors.

```html
<!DOCTYPE html>
<html lang="en">
<head>
<meta charset="utf-8">
<title>Memorial Ledger Suite</title>
<link href="https://fonts.googleapis.com/css2?family=Roboto:wght@400;500;700;900&display=swap" rel="stylesheet">
<style>
:root{
  --yellow:#fbee3d;
  --gold:#f5c400;
  --black:#000000;
  --grey:#5c5c5c;
  --dark:#3b3b3b;
  --darker:#2a2a2a;
  --ink:#222222;
  --muted:#6d6d6d;
  --line:#e4e4e4;
  --mist:#eef1f4;
  --white:#ffffff;
}
*{margin:0;padding:0;box-sizing:border-box}
html,body{width:1200px;height:4523px;overflow:hidden}
body{position:relative;background:var(--white);font-family:"Roboto",Arial,sans-serif;color:var(--ink)}
.abs{position:absolute}
/* header */
.site-header{position:absolute;left:0;top:0;width:1200px;height:166px;background:var(--white)}
.brand{position:absolute;left:111px;top:62px;display:flex;align-items:center;gap:10px;font-weight:900;font-size:24px;color:var(--gold);letter-spacing:.5px;text-transform:uppercase}
.brand-dot{width:16px;height:16px;border-radius:50%;background:var(--gold)}
.main-nav{position:absolute;right:115px;top:74px;display:flex;gap:30px;font-size:17px;font-weight:500;color:var(--ink);align-items:center}
/* hero */
.hero{position:absolute;left:0;top:166px;width:1200px;height:664px;overflow:hidden}
.hero-photo{position:absolute;inset:0;background:linear-gradient(100deg,#6e5a45 0%,#8b7560 30%,#c9c2bb 55%,#e9e6e3 75%,#3c3431 100%)}
.hero-title{position:absolute;left:111px;top:196px;font-size:44px;font-weight:700;color:var(--white);letter-spacing:.5px}
.hero-sub{position:absolute;left:111px;top:258px;width:520px;font-size:18px;font-weight:700;line-height:27px;color:var(--white)}
.btn{display:inline-flex;align-items:center;justify-content:center;gap:6px;background:var(--yellow);color:var(--black);font-weight:700;text-transform:uppercase;border-radius:30px}
.hero-btn{position:absolute;left:111px;top:342px;width:160px;height:42px;font-size:14px}
.slide-arrow{position:absolute;width:34px;height:34px;border-radius:50%;display:flex;align-items:center;justify-content:center}
/* sections */
.section-title{position:absolute;left:0;width:1200px;text-align:center;font-size:42px;font-weight:900;color:var(--black);text-transform:uppercase}
.features{position:absolute;left:0;top:830px;width:1200px;height:980px;background:linear-gradient(180deg,#ffffff 0%,#f4f4f4 60%,#e9e9e9 100%)}
.feature-card{position:absolute;width:303px;height:233px;background:var(--white);border:1px solid var(--line);box-shadow:0 2px 8px rgba(0,0,0,.06);text-align:center}
.feature-card svg{position:absolute;left:121px;top:26px}
.feature-card h3{position:absolute;left:0;top:102px;width:100%;font-size:19px;font-weight:500;color:var(--ink)}
.feature-card p{position:absolute;left:30px;top:134px;width:243px;font-size:13px;line-height:23px;color:var(--muted)}
.features-btn{position:absolute;left:461px;top:777px;width:278px;height:60px;font-size:17px}
/* team */
.team{position:absolute;left:0;top:1780px;width:1200px;height:700px}
.member{position:absolute;width:300px;text-align:center;color:var(--white)}
.member .portrait{width:160px;height:160px;border-radius:50%;margin:0 auto;border:4px solid var(--white);background:radial-gradient(circle at 50% 40%,#d9c3b0 0%,#9c8a7c 55%,#e6e6e6 100%)}
.member h4{margin-top:22px;font-size:18px;font-weight:700;text-transform:uppercase}
.member p{margin-top:6px;font-size:13px;line-height:24px;color:#dcdcdc}
.socials{margin-top:10px;display:flex;justify-content:center;gap:9px}
.socials span{width:11px;height:11px;border-radius:50%;background:var(--white)}
/* steps */
.step{position:absolute;left:111px;width:392px;height:128px;border-bottom:2px solid var(--line);padding-left:50px}
.step.alt{background:#f2f2f2}
.step .tick{position:absolute;left:8px;top:22px}
.step h5{margin-top:20px;font-size:15px;font-weight:700;text-transform:uppercase}
.step p{margin-top:14px;font-size:13px;line-height:24px;color:var(--muted)}
/* testimonials */
.testimonials{position:absolute;left:0;top:3114px;width:1200px;height:490px;background:linear-gradient(180deg,#e6ebf0,#f3f5f7)}
.quote{position:absolute;width:330px;height:180px}
.quote .avatar{position:absolute;left:0;top:0;width:62px;height:62px;border-radius:50%;background:radial-gradient(circle at 50% 40%,#c9a48a,#6f5646)}
.quote .stars{position:absolute;left:82px;top:-34px;color:var(--gold);font-size:16px;letter-spacing:1px}
.quote blockquote{position:absolute;left:82px;top:-8px;width:230px;font-size:12.5px;line-height:21px;color:var(--muted);font-style:italic}
.quote h6{position:absolute;left:82px;top:90px;font-size:14px;font-weight:700;text-transform:uppercase}
.quote span.role{position:absolute;left:82px;top:116px;font-size:12.5px;color:var(--muted)}
.dots{position:absolute;left:560px;top:415px;display:flex;gap:8px}
.dots i{width:11px;height:11px;border-radius:50%;border:1px solid #9a9a9a;display:block}
.dots i.on{background:var(--gold);border-color:var(--gold)}
/* stay connected */
.connect{position:absolute;left:0;top:3600px;width:1200px;height:540px;overflow:hidden}
.field{position:absolute;top:232px;height:36px;border-bottom:2px solid var(--dark);font-size:14px;color:var(--ink);padding:6px 0 0 2px}
.subscribe-btn{position:absolute;left:497px;top:306px;width:205px;height:46px;background:var(--black);color:var(--white);border-radius:30px;font-size:16px;font-weight:700;display:flex;align-items:center;justify-content:center;letter-spacing:.5px}
/* footer */
.site-footer{position:absolute;left:0;top:4100px;width:1200px;height:332px;background:var(--dark);color:var(--white)}
.footer-brand{position:absolute;left:111px;top:96px;font-size:24px;font-weight:900;text-transform:uppercase;color:var(--white);width:260px;line-height:32px}
.footer-social{position:absolute;left:140px;top:240px;display:flex;gap:14px}
.footer-social span{width:36px;height:36px;border-radius:50%;border:2px solid var(--white)}
.footer-col h5{font-size:16px;font-weight:700;text-transform:uppercase;margin-bottom:24px}
.contact-item{display:flex;gap:16px;font-size:14px;line-height:22px;margin-bottom:18px;align-items:flex-start}
.news-input{margin-top:18px;width:240px;height:34px;border:1px solid #8a8a8a;font-size:13px;padding:8px 10px;color:#d0d0d0}
.news-btn{margin-top:18px;width:108px;height:36px;font-size:12px}
.legal{position:absolute;left:0;top:4432px;width:1200px;height:91px;background:var(--darker);color:#e0e0e0;font-size:14px;text-align:center;line-height:91px}
</style>
</head>
<body>

<header class="site-header">
  <div class="brand"><span class="brand-dot"></span>Memorial Ledger Suite</div>
  <nav class="main-nav">
    <span>HOME</span><span>ABOUT US</span><span>SERVICES</span><span>GALLERY</span><span>CONTACT</span>
    <svg width="18" height="18" viewBox="0 0 18 18"><circle cx="7.5" cy="7.5" r="5.5" fill="none" stroke="#222" stroke-width="2.4"/><line x1="11.5" y1="11.5" x2="16.5" y2="16.5" stroke="#222" stroke-width="2.6" stroke-linecap="round"/></svg>
  </nav>
</header>

<section class="hero">
  <div class="hero-photo" role="img" aria-label="Photo of a mourner in black placing a red rose on a wooden casket"></div>
  <h1 class="hero-title">MEMORIAL LEDGER</h1>
  <p class="hero-sub">Lorem ipsum dolor sit amet consectetur adipiscing elit eiusmod tempor incididunt ut labore.</p>
  <span class="btn hero-btn">Read more
    <svg width="14" height="14" viewBox="0 0 14 14"><circle cx="7" cy="7" r="7" fill="#000"/><path d="M5.5 4l3 3-3 3" stroke="#fbee3d" stroke-width="1.8" fill="none"/></svg></span>
  <div class="slide-arrow" style="left:26px;top:248px;background:rgba(0,0,0,.55)"><svg width="12" height="12" viewBox="0 0 12 12"><path d="M8 1L3 6l5 5" stroke="#fff" stroke-width="2" fill="none"/></svg></div>
  <div class="slide-arrow" style="left:1140px;top:248px"><svg width="12" height="12" viewBox="0 0 12 12"><path d="M4 1l5 5-5 5" stroke="#fff" stroke-width="2" fill="none"/></svg></div>
  <svg class="abs" style="left:0;top:0" width="1200" height="664" viewBox="0 0 1200 664">
    <path d="M0 545 C250 690 750 700 1200 505 L1200 664 L0 664Z" fill="#fff"/>
    <path d="M180 640 C560 700 900 640 1200 495" stroke="#f5c400" stroke-width="11" fill="none"/>
  </svg>
</section>

<section class="features">
  <h2 class="section-title" style="top:120px">Our Features</h2>

  <article class="feature-card" style="left:111px;top:219px">
    <svg width="60" height="60" viewBox="0 0 60 60"><path d="M16 40a10 10 0 0 1 2-20 14 14 0 0 1 26 3 9 9 0 0 1 0 17z" fill="#fbee3d" stroke="#555" stroke-width="2"/><line x1="30" y1="40" x2="30" y2="52" stroke="#555" stroke-width="2"/><circle cx="30" cy="54" r="3" fill="#555"/></svg>
    <h3>Online Software</h3>
    <p>Lorem ipsum dolor sit consectetur adipiscing elit, sed do eiusmod tempor incididunt ut labore aliqua.</p>
  </article>
  <article class="feature-card" style="left:449px;top:219px">
    <svg width="60" height="60" viewBox="0 0 60 60"><rect x="14" y="6" width="30" height="40" fill="#fff" stroke="#555" stroke-width="2"/><rect x="20" y="12" width="30" height="40" fill="#fff" stroke="#555" stroke-width="2"/><line x1="25" y1="22" x2="45" y2="22" stroke="#555" stroke-width="2"/><line x1="25" y1="29" x2="45" y2="29" stroke="#555" stroke-width="2"/><line x1="25" y1="36" x2="40" y2="36" stroke="#555" stroke-width="2"/><circle cx="46" cy="48" r="7" fill="#fbee3d" stroke="#555" stroke-width="2"/></svg>
    <h3>Personalized Documents</h3>
    <p>Lorem ipsum dolor sit consectetur adipiscing elit, sed do eiusmod tempor incididunt ut labore aliqua.</p>
  </article>
  <article class="feature-card" style="left:784px;top:219px">
    <svg width="60" height="60" viewBox="0 0 60 60"><circle cx="30" cy="30" r="16" fill="#fbee3d" stroke="#555" stroke-width="2" stroke-dasharray="6 3"/><circle cx="30" cy="30" r="7" fill="#fff" stroke="#555" stroke-width="2"/><path d="M30 6v6M30 48v6M6 30h6M48 30h6" stroke="#555" stroke-width="3"/></svg>
    <h3>Customization</h3>
    <p>Lorem ipsum dolor sit consectetur adipiscing elit, sed do eiusmod tempor incididunt ut labore aliqua.</p>
  </article>
  <article class="feature-card" style="left:111px;top:481px">
    <svg width="60" height="60" viewBox="0 0 60 60"><rect x="6" y="14" width="48" height="32" rx="3" fill="#fff" stroke="#555" stroke-width="2"/><rect x="11" y="20" width="14" height="16" fill="#fbee3d" stroke="#555" stroke-width="1.5"/><line x1="30" y1="22" x2="48" y2="22" stroke="#555" stroke-width="2"/><line x1="30" y1="29" x2="48" y2="29" stroke="#555" stroke-width="2"/><line x1="30" y1="36" x2="42" y2="36" stroke="#555" stroke-width="2"/></svg>
    <h3>Electronic Identity Card</h3>
    <p>Lorem ipsum dolor sit consectetur adipiscing elit, sed do eiusmod tempor incididunt ut labore aliqua.</p>
  </article>
  <article class="feature-card" style="left:449px;top:481px">
    <svg width="60" height="60" viewBox="0 0 60 60"><path d="M18 42V28a12 12 0 0 1 24 0v14l4 4H14z" fill="#fff" stroke="#555" stroke-width="2"/><circle cx="30" cy="50" r="4" fill="#555"/><circle cx="40" cy="20" r="7" fill="#fbee3d" stroke="#555" stroke-width="2"/></svg>
    <h3>Notifications</h3>
    <p>Lorem ipsum dolor sit consectetur adipiscing elit, sed do eiusmod tempor incididunt ut labore aliqua.</p>
  </article>
  <article class="feature-card" style="left:784px;top:481px">
    <svg width="60" height="60" viewBox="0 0 60 60"><rect x="6" y="10" width="42" height="30" rx="2" fill="#fff" stroke="#555" stroke-width="2"/><line x1="27" y1="40" x2="27" y2="48" stroke="#555" stroke-width="2"/><line x1="18" y1="49" x2="36" y2="49" stroke="#555" stroke-width="2"/><rect x="40" y="28" width="14" height="24" rx="2" fill="#fbee3d" stroke="#555" stroke-width="2"/></svg>
    <h3>Display On Screens</h3>
    <p>Lorem ipsum dolor sit consectetur adipiscing elit, sed do eiusmod tempor incididunt ut labore aliqua.</p>
  </article>

  <span class="btn features-btn">View all features
    <svg width="16" height="16" viewBox="0 0 14 14"><circle cx="7" cy="7" r="7" fill="#000"/><path d="M5.5 4l3 3-3 3" stroke="#fbee3d" stroke-width="1.8" fill="none"/></svg></span>
</section>

<section class="team">
  <svg class="abs" style="left:0;top:0" width="1200" height="700" viewBox="0 0 1200 700">
    <defs><linearGradient id="teamBg" x1="0" y1="0" x2="1" y2="0"><stop offset="0" stop-color="#3a3a3a"/><stop offset=".5" stop-color="#4a4a4a"/><stop offset="1" stop-color="#353535"/></linearGradient></defs>
    <path d="M0 140 C380 60 800 10 1200 40 L1200 545 C900 600 500 720 0 600Z" fill="url(#teamBg)" role="img" aria-label="Dark photo of mourners gathered at a memorial"/>
    <path d="M0 140 C380 60 800 10 1200 40" stroke="#f5c400" stroke-width="10" fill="none"/>
    <path d="M0 600 C300 680 560 690 820 630" stroke="#f5c400" stroke-width="10" fill="none"/>
  </svg>
  <h2 class="section-title" style="top:185px;color:var(--white)">Our Team</h2>
  <div class="member" style="left:97px;top:285px">
    <div class="portrait" role="img" aria-label="Portrait photo of team member"></div>
    <h4>Dorian Vale</h4>
    <p>Nam libero tempore, cum soluta nobis eligendi<br>optio cumque nihil impedit quo minus facere</p>
    <div class="socials"><span></span><span></span><span></span></div>
  </div>
  <div class="member" style="left:450px;top:285px">
    <div class="portrait" role="img" aria-label="Portrait photo of team member"></div>
    <h4>Selene Marlow</h4>
    <p>Nam libero tempore, cum soluta nobis eligendi<br>optio cumque nihil impedit quo minus facere</p>
    <div class="socials"><span></span><span></span><span></span></div>
  </div>
  <div class="member" style="left:803px;top:285px">
    <div class="portrait" role="img" aria-label="Portrait photo of team member"></div>
    <h4>Julian Frost</h4>
    <p>Nam libero tempore, cum soluta nobis eligendi<br>optio cumque nihil impedit quo minus facere</p>
    <div class="socials"><span></span><span></span><span></span></div>
  </div>
</section>

<section class="steps">
  <div class="step" style="top:2630px">
    <svg class="tick" width="24" height="24" viewBox="0 0 24 24"><circle cx="12" cy="12" r="10" fill="none" stroke="#f5c400" stroke-width="2"/><path d="M7 12l3.5 3.5L17 9" stroke="#f5c400" stroke-width="2.2" fill="none"/></svg>
    <h5>Register now</h5>
    <p>Lorem ipsum dolor met consectetur adipiscing elit, sed do eiusmod tempor incididunt...</p>
  </div>
  <div class="step alt" style="top:2758px">
    <svg class="tick" width="24" height="24" viewBox="0 0 24 24"><circle cx="12" cy="12" r="10" fill="none" stroke="#f5c400" stroke-width="2"/><path d="M7 12l3.5 3.5L17 9" stroke="#f5c400" stroke-width="2.2" fill="none"/></svg>
    <h5>Follow our procedures</h5>
    <p>Lorem ipsum dolor met consectetur adipiscing elit, sed do eiusmod tempor incididunt...</p>
  </div>
  <div class="step" style="top:2886px">
    <svg class="tick" width="24" height="24" viewBox="0 0 24 24"><circle cx="12" cy="12" r="10" fill="none" stroke="#f5c400" stroke-width="2"/><path d="M7 12l3.5 3.5L17 9" stroke="#f5c400" stroke-width="2.2" fill="none"/></svg>
    <h5>Get a notifications</h5>
    <p>Lorem ipsum dolor met consectetur adipiscing elit, sed do eiusmod tempor incididunt...</p>
  </div>

  <svg class="abs" style="left:555px;top:2650px" width="585" height="345" viewBox="0 0 585 345">
    <defs><linearGradient id="screenFill" x1="0" y1="0" x2="1" y2="1"><stop offset="0" stop-color="#f4f5f7"/><stop offset="1" stop-color="#dfe3e8"/></linearGradient></defs>
    <rect x="58" y="2" width="470" height="316" rx="14" fill="#1d1d1d"/>
    <rect x="74" y="18" width="438" height="284" fill="url(#screenFill)" role="img" aria-label="Screenshot of the software dashboard with charts and reports"/>
    <path d="M0 318 H585 L570 334 Q560 342 540 342 H45 Q25 342 15 334Z" fill="#c8cbd0"/>
    <rect x="250" y="318" width="85" height="8" rx="4" fill="#9da1a8"/>
  </svg>
</section>

<section class="testimonials">
  <h2 class="section-title" style="top:95px">Our Testimonials</h2>
  <div class="slide-arrow" style="left:30px;top:252px"><svg width="12" height="14" viewBox="0 0 12 14"><path d="M8 1L3 7l5 6" stroke="#555" stroke-width="2" fill="none"/></svg></div>
  <div class="slide-arrow" style="left:1132px;top:252px"><svg width="12" height="14" viewBox="0 0 12 14"><path d="M4 1l5 6-5 6" stroke="#555" stroke-width="2" fill="none"/></svg></div>

  <div class="quote" style="left:112px;top:200px">
    <div class="avatar" role="img" aria-label="Client portrait photo"></div>
    <span class="stars">★★★★★</span>
    <blockquote>“ At vero eos et accusamus et iusto odio dignissimos ducimus qui blanditiis praesentium voluptatum deleniti atque corrupti quos dolores quas molestias ”</blockquote>
    <h6>Nadia Cole</h6>
    <span class="role">Creative Manager, USA</span>
  </div>
  <div class="quote" style="left:452px;top:200px">
    <div class="avatar" role="img" aria-label="Client portrait photo"></div>
    <span class="stars">★★★★★</span>
    <blockquote>“ At vero eos et accusamus et iusto odio dignissimos ducimus qui blanditiis praesentium voluptatum deleniti atque corrupti quos dolores quas molestias ”</blockquote>
    <h6>Owen Harte</h6>
    <span class="role">Events Manager, USA</span>
  </div>
  <div class="quote" style="left:792px;top:200px">
    <div class="avatar" role="img" aria-label="Client portrait photo"></div>
    <span class="stars">★★★★★</span>
    <blockquote>“ At vero eos et accusamus et iusto odio dignissimos ducimus qui blanditiis praesentium voluptatum deleniti atque corrupti quos dolores quas molestias ”</blockquote>
    <h6>Elias Brandt</h6>
    <span class="role">Team Manager, USA</span>
  </div>
  <div class="dots"><i></i><i></i><i class="on"></i><i></i><i></i></div>
</section>

<section class="connect">
  <svg class="abs" style="left:0;top:0" width="1200" height="540" viewBox="0 0 1200 540">
    <defs><linearGradient id="connectBg" x1="0" y1="0" x2="1" y2="1"><stop offset="0" stop-color="#fbee3d"/><stop offset=".55" stop-color="#f2d21c"/><stop offset="1" stop-color="#d9b400"/></linearGradient></defs>
    <rect width="1200" height="540" fill="url(#connectBg)" role="img" aria-label="Yellow-toned photo of a memorial gathering"/>
    <path d="M0 0 H1200 V60 C800 0 400 0 0 90Z" fill="#f3f5f7"/>
    <path d="M0 430 C300 560 800 560 1200 390 L1200 540 L0 540Z" fill="#3b3b3b"/>
    <path d="M0 430 C300 560 800 560 1200 390" stroke="#9a9a9a" stroke-width="5" fill="none"/>
  </svg>
  <h2 class="section-title" style="top:138px">Stay Connected</h2>
  <div class="field" style="left:220px;width:368px">Enter Name</div>
  <div class="field" style="left:612px;width:365px">Enter Email</div>
  <span class="subscribe-btn">SUBSCRIBE</span>
</section>

<footer class="site-footer">
  <div class="footer-brand">Memorial Ledger Suite</div>
  <div class="footer-social"><span></span><span></span><span></span><span></span></div>

  <div class="footer-col abs" style="left:443px;top:102px;width:330px">
    <h5>Contact Us</h5>
    <div class="contact-item">
      <svg width="14" height="18" viewBox="0 0 14 18"><path d="M7 0a7 7 0 0 1 7 7c0 5-7 11-7 11S0 12 0 7a7 7 0 0 1 7-7z" fill="#fff"/><circle cx="7" cy="7" r="2.5" fill="#3b3b3b"/></svg>
      <span>742 Cedar Lane, Brookfield, CA<br>Lakeside, USA</span>
    </div>
    <div class="contact-item">
      <svg width="14" height="16" viewBox="0 0 14 16"><path d="M3 0l3 4-2 2c1 2 3 4 5 5l2-2 3 3-2 3C6 15 0 9 0 3z" fill="#fff"/></svg>
      <span>(+100) 555 014 2880</span>
    </div>
    <div class="contact-item">
      <svg width="16" height="12" viewBox="0 0 16 12"><rect width="16" height="12" fill="#fff"/><path d="M0 0l8 7 8-7" stroke="#3b3b3b" stroke-width="1.5" fill="none"/></svg>
      <span>hello@memorialledger.example</span>
    </div>
  </div>

  <div class="footer-col abs" style="left:820px;top:102px;width:280px">
    <h5>Newsletter Subscription</h5>
    <p style="font-size:14px;line-height:22px">Register your Email Address to get more<br>information about us</p>
    <div class="news-input">Email Address</div>
    <span class="btn news-btn">Subscribe</span>
  </div>
</footer>

<div class="legal">Copyrights © 2019 Memorial Ledger Suite. All Rights Reserved &nbsp; | &nbsp; Privacy Policy.</div>

</body>
</html>
```